Hip, Modern Home Page for Successful SEO Expert

Dorian Wexley is an SEO expert, author and professional speaker. His site is
www.dorianwexley.example. We need a re-design of the website so that it does not look outdated or like an off-the-shelf Wordpress template (like it currently does). The new design must convey to the visitor a compelling call-to-action. Specially, this home page will act as a “squeeze page” and thus, the primary marketing goal will be to get the user to opt in to our list. The new design will provide elements of “social proof” such as written testimonials, a portfolio of case studies, client logos, “as appeared on” logos, client testimonial video, etc.
Updates

Please incorporate the recently uploaded headshots into your design 

Target Market(s)

People looking for help in internet marketing for their websites, entrepreneurs, start-ups, bloggers, companies looking to build an online presence, conferences looking to book Dorian for speaking. Small business people and SEO newbies interested in buying Dorian’s video-based training (CraftofRanking.example).

Industry/Entity Type

Marketing

Font styles to use
Sans Serif

Colors
f68d4d
3276b5
8769ae
acd036

Requirements
Must have
• strong call to action
Should not have
• should not look like a template. should not use old style fonts. should not have more than one page scroll

```html
<!DOCTYPE html>
<html lang="en">
<head>
<meta charset="utf-8">
<title>Dorian Wexley — SEO Expert, Author, Professional Speaker</title>
<link rel="stylesheet" href="https://fonts.googleapis.com/css2?family=Bebas+Neue&family=Lato:ital,wght@0,400;0,700;1,400&display=swap">
<style>
  :root {
    --ink: #262626;
    --panel: #333333;
    --white: #ffffff;
    --field: #f4f4f4;
    --lime: #acd036;
    --blue: #3276b5;
    --band: rgba(255,255,255,0.55);
    --muted: #555555;
  }
  * { box-sizing: border-box; margin: 0; padding: 0; }
  html, body { width: 1200px; height: 906px; overflow: hidden; background: var(--white); }
  body { position: relative; font-family: "Lato", sans-serif; color: var(--ink); }

  .hero { position: absolute; left: 0; top: 0; width: 1200px; height: 628px; overflow: hidden; }
  .hero-photo {
    position: absolute; inset: 0;
    background:
      radial-gradient(ellipse 260px 330px at 330px 360px, #6f7686 0%, #8a93a6 45%, rgba(200,205,212,0) 100%),
      linear-gradient(180deg, #c9c5c0 0%, #e8e8e6 12%, #f3f3f2 40%, #ebeced 75%, #d9dcdf 100%);
  }
  .main-nav { position: absolute; top: 36px; right: 57px; display: flex; gap: 38px; }
  .main-nav a {
    font-family: "Bebas Neue", sans-serif; font-size: 29px; letter-spacing: 0.5px;
    color: var(--white); text-decoration: none; text-shadow: 2px 2px 2px rgba(0,0,0,0.55);
  }
  .name-band { position: absolute; left: 0; top: 511px; width: 1200px; height: 117px; background: var(--band); }
  .hero-name {
    position: absolute; left: 120px; top: 516px;
    font-family: "Bebas Neue", sans-serif; font-weight: 400; font-size: 78px; line-height: 1;
    letter-spacing: 1px; color: var(--ink);
  }
  .hero-role { position: absolute; left: 113px; top: 590px; font-size: 22px; color: var(--ink); }

  .optin {
    position: absolute; left: 712px; top: 154px; width: 390px; height: 474px;
    background: var(--panel); border-radius: 8px 8px 0 0; color: var(--white); text-align: center;
  }
  .optin h2 { margin-top: 52px; font-size: 29px; font-weight: 700; line-height: 36px; }
  .optin p { margin: 12px auto 0; width: 320px; font-size: 18px; line-height: 24px; }
  .optin .email {
    position: absolute; left: 39px; top: 288px; width: 312px; height: 54px;
    background: var(--field); border: 2px solid #1e1e1e; border-radius: 3px;
    font: 400 19px "Lato", sans-serif; color: #888; padding-left: 10px; text-align: left;
  }
  .optin .cta {
    position: absolute; left: 66px; top: 368px; width: 259px; height: 55px;
    background: var(--lime); border: 0; border-radius: 2px;
    font: 400 20px "Lato", sans-serif; color: #2a2a2a;
  }

  .divider { position: absolute; left: 0; top: 628px; width: 1200px; height: 3px; background: var(--panel); }

  .section-title { font-family: "Bebas Neue", sans-serif; font-weight: 400; font-size: 40px; line-height: 1; color: var(--ink); }
  .portfolio .section-title { position: absolute; left: 57px; top: 658px; }
  .carousel-arrows { position: absolute; left: 536px; top: 663px; }
  .thumb { position: absolute; top: 715px; width: 200px; height: 150px; }
  .thumb-1 { left: 57px; background: linear-gradient(135deg, #6a4a3a, #4d3a30 60%, #5d6f6a); }
  .thumb-2 { left: 297px; background: linear-gradient(180deg, #8fc04a, #6fa534); }
  .thumb-2::after { content: ""; position: absolute; left: 12px; right: 12px; top: 10px; bottom: 0; background: #f7f7f7; }
  .thumb-3 { left: 536px; width: 64px; background: linear-gradient(135deg, #6a2536, #4a1a2a); }

  .testimonial {
    position: absolute; left: 600px; top: 631px; width: 236px; height: 234px;
    background: var(--blue); color: var(--white); text-align: center; font-style: italic;
    padding: 30px 20px 0; font-size: 15px; line-height: 19.5px;
  }
  .testimonial blockquote { font-style: normal; }
  .testimonial cite { display: block; margin-top: 18px; font-style: italic; }

  .blog .section-title { position: absolute; left: 865px; top: 658px; }
  .blog ul { position: absolute; left: 865px; top: 710px; width: 300px; list-style: none; }
  .blog li { font-size: 17px; line-height: 22px; margin-bottom: 9px; }
  .blog a { color: var(--ink); text-decoration: none; }
</style>
</head>
<body>
  <header class="hero">
    <div class="hero-photo" role="img" aria-label="Portrait of Dorian Wexley, arms crossed, in a grey vest before a blurred waterfront"></div>
    <nav class="main-nav">
      <a href="#">About</a><a href="#">Blog</a><a href="#">Speaking</a><a href="#">Contact</a>
    </nav>
    <div class="name-band"></div>
    <h1 class="hero-name">Dorian Wexley</h1>
    <p class="hero-role">SEO Expert, Author, Professional Speaker</p>
    <form class="optin">
      <h2>Learn how you can<br>make $10,000/month<br>Blogging 2 hours a day.</h2>
      <p>Lorem ipsum dolor sit amet, consec&shy;tetur adipiscing elit. Integer aliquet lobortis purus. Pellentesque pellen&shy;tesque eleifend leo.</p>
      <input class="email" type="email" placeholder="Your Email">
      <button class="cta" type="button">Get It Now</button>
    </form>
  </header>

  <div class="divider"></div>

  <section class="portfolio">
    <h2 class="section-title">Portfolio</h2>
    <svg class="carousel-arrows" width="56" height="28" viewBox="0 0 56 28" aria-hidden="true">
      <polygon points="14,2 0,14 14,26" fill="#555"/>
      <polygon points="37,2 51,14 37,26" fill="#555"/>
    </svg>
    <div class="thumb thumb-1" role="img" aria-label="Case study: illustrated character portrait cards"></div>
    <div class="thumb thumb-2" role="img" aria-label="Case study: weekly calendar app interface"></div>
    <div class="thumb thumb-3" role="img" aria-label="Case study: illustrated figure at a desk"></div>
  </section>

  <aside class="testimonial">
    <blockquote>“Dorian Wexley is the SEO master. Anyone who wants to know how SEO really works must read The Ranking Handbook. This is a true reference work. ”</blockquote>
    <cite>- Marcus Lindqvist, Superblogger<br>www.marcuslindqvist.example</cite>
  </aside>

  <section class="blog">
    <h2 class="section-title">Blog Posts</h2>
    <ul>
      <li><a href="#">Microdata and Vocabra.example for all your Searchly rich snippet needs</a></li>
      <li><a href="#">How to Restart a Blog When You’ve Been on Hiatus for Three Years</a></li>
      <li><a href="#">The Convergence of Nanotech, Biotech, Infotech, Cognitive Science</a></li>
    </ul>
  </section>
</body>
</html>
```